Kolmister Technologies LOGO, Business Card, and Stationary Project
Kolmister Technologies
Kolmister Technologies LOGO, Business Card, and Stationary Project - Consulting
Creative Brief
Modern
Tobias Whelkin
President / CEO
417 North Pellham Road # Harlowfield, Westmarch 20964
twhelkin@kolmister-example.com
www.kolmister-example.com
Note to Winner: The final files created for this project will need to be sent to the Project Holder to allow for updates to address or adding new employees to business cards or stationary. Ensure that final copies are sent unlayerd in Adobe PSD format.
We Shape the Digital Tomorrow Right Now

```html
<!DOCTYPE html>
<html lang="en">
<head>
<meta charset="utf-8">
<title>Kolmister Technologies – Business Card</title>
<link href="https://fonts.googleapis.com/css2?family=Arimo:ital,wght@0,400;0,700;1,700&display=swap" rel="stylesheet">
<style>
  :root {
    --stage: #e9e9e9;
    --card: #ffffff;
    --brand-red: #c4161c;
    --deep-red: #8e0c10;
    --swoosh-grey: #b9b9b9;
    --ink: #1e1e1e;
    --tag-blue: #17305f;
    --faint-blush: #f6e6e2;
  }
  * { margin: 0; padding: 0; box-sizing: border-box; }
  html, body { width: 1200px; height: 899px; overflow: hidden; background: var(--stage); }
  body { position: relative; font-family: "Arimo", Arial, sans-serif; }
  .card {
    position: absolute; background: var(--card); border-radius: 20px; overflow: hidden;
    box-shadow: 0 6px 18px rgba(0,0,0,.25);
  }
  .card svg.art { position: absolute; inset: 0; }
  .card-front { left: 92px; top: 73px; width: 681px; height: 425px; }
  .card-back { left: 425px; top: 445px; width: 698px; height: 393px; }

  .brand { position: absolute; display: flex; align-items: center; gap: 12px; }
  .brand-mark { width: 46px; height: 46px; border-radius: 50%; background: var(--brand-red); flex: none; }
  .brand-name { color: var(--brand-red); font-weight: 700; font-size: 30px; white-space: nowrap; }
  .card-front .brand { left: 228px; top: 40px; }

  .holder { position: absolute; left: 408px; top: 222px; color: var(--ink); }
  .holder-name { font-size: 23px; font-weight: 400; }
  .holder-title { font-size: 17px; margin-top: 8px; padding-left: 14px; }

  .contact { position: absolute; left: 22px; top: 234px; color: #fff; font-size: 13px; line-height: 17px; font-style: normal; }
  .contact .gap { height: 17px; }
  .web { position: absolute; left: 22px; bottom: 22px; color: #fff; font-size: 13px; }

  .card-back .brand { right: 30px; bottom: 78px; }
  .card-back .brand-name { font-size: 33px; }
  .tagline {
    position: absolute; right: 30px; bottom: 38px; color: var(--tag-blue);
    font-size: 18px; font-weight: 700; font-style: italic; white-space: nowrap;
  }
</style>
</head>
<body>

<section class="card card-front" aria-label="Business card front">
  <svg class="art" width="681" height="425" viewBox="0 0 681 425">
    <defs>
      <linearGradient id="redField" x1="0" y1="0" x2="1" y2="1">
        <stop offset="0" stop-color="#d3242a"/>
        <stop offset="1" stop-color="#8e0c10"/>
      </linearGradient>
    </defs>
    <path d="M0 190 C140 185 250 240 330 320 C370 360 400 395 420 425 L0 425 Z" fill="url(#redField)"/>
    <path d="M0 175 C180 150 330 230 440 320 C500 368 560 400 681 410" fill="none" stroke="var(--swoosh-grey)" stroke-width="9"/>
    <path d="M0 160 C200 130 360 210 470 300 C540 355 610 385 681 390" fill="none" stroke="#d6d6d6" stroke-width="4"/>
  </svg>
  <div class="brand">
    <span class="brand-mark"></span>
    <span class="brand-name">Kolmister Technologies</span>
  </div>
  <div class="holder">
    <p class="holder-name">Tobias Whelkin</p>
    <p class="holder-title">President / CEO</p>
  </div>
  <address class="contact">
    <p>417 North Pellham Road #</p>
    <p>Harlowfield</p>
    <p>Westmarch 20964</p>
    <div class="gap"></div>
    <p>P: 555.203.0142</p>
    <p>F: 555.458.0187</p>
    <p>E: twhelkin@kolmister-example.com</p>
  </address>
  <p class="web">www.kolmister-example.com</p>
</section>

<section class="card card-back" aria-label="Business card back">
  <svg class="art" width="698" height="393" viewBox="0 0 698 393">
    <circle cx="170" cy="170" r="150" fill="var(--faint-blush)"/>
  </svg>
  <div class="brand">
    <span class="brand-mark"></span>
    <span class="brand-name">Kolmister Technologies</span>
  </div>
  <p class="tagline">We Shape the Digital Tomorrow Right Now</p>
</section>

</body>
</html>
```